■デザインへの要望
1)フライヤーのイメージとしては明るく女性的なイメージを希望します。
2)人物写真は使わないでください。
3)コーポレートロゴを右上に配置してください。
ロゴの改変(色の変更や比率の変更)はご遠慮ください。
4)会のロゴを配置してください。
位置はお任せしますが、サイズの変更はご遠慮ください。
※前回のフライヤーを素材と一緒にお付けしますのでご参考になさってください。

■素材
1)フライヤーを作成する際に必要なロゴ等の画像等は

```html
<!DOCTYPE html>
<html lang="ja">
<head>
<meta charset="utf-8">
<title>これからの摂食嚥下障害看護に何が求められているか</title>
<link rel="stylesheet" href="https://fonts.googleapis.com/css2?family=Noto+Sans+JP:wght@400;500;700;900&display=swap">
<style>
  :root {
    --white: #ffffff;
    --ink: #3a4a5a;
    --sky-deep: #3aa2e0;
    --sky-mid: #6cc2ee;
    --sky-light: #b5e2f7;
    --label-blue: #2a8fd4;
  }
  * { margin: 0; padding: 0; box-sizing: border-box; }
  html, body { width: 849px; height: 1200px; overflow: hidden; background: var(--white); }
  body { font-family: "Noto Sans JP", sans-serif; color: var(--ink); }
  .flyer { position: relative; width: 849px; height: 1200px; background: var(--white); overflow: hidden; }

  .masthead { position: absolute; left: 0; top: 0; width: 849px; height: 198px; }
  .society-name { position: absolute; left: 52px; top: 40px; font-size: 20px; font-weight: 500; color: var(--ink); letter-spacing: 3px; }
  .conference-name { position: absolute; left: 52px; top: 118px; font-size: 22px; font-weight: 500; color: var(--ink); letter-spacing: 0.5px; }
  .sponsor-name { position: absolute; right: 40px; top: 34px; font-size: 26px; font-weight: 500; color: var(--ink); letter-spacing: 2px; }

  .hero { position: absolute; left: 0; top: 198px; width: 849px; height: 922px;
    background:
      radial-gradient(circle at 20% 30%, rgba(255,255,255,0.28), transparent 40%),
      radial-gradient(circle at 85% 80%, rgba(255,255,255,0.25), transparent 45%),
      linear-gradient(160deg, var(--sky-deep) 0%, var(--sky-mid) 50%, var(--sky-light) 100%); }

  .title { position: absolute; left: 120px; top: 50px; color: var(--white); font-weight: 900; font-size: 60px; line-height: 70px; letter-spacing: 2px;
    text-shadow: 0 2px 6px rgba(20,80,140,0.35); }
  .subtitle { position: absolute; left: 0; width: 849px; top: 264px; text-align: center; color: var(--white); font-size: 26px; font-weight: 700; line-height: 36px; }
  .subtitle-en { position: absolute; left: 0; width: 849px; top: 302px; text-align: center; color: var(--white); font-size: 17px; font-style: italic; letter-spacing: 0.5px; line-height: 24px; }
  .rule { position: absolute; left: 120px; width: 609px; top: 332px; height: 2px; background: var(--white); }

  .date { position: absolute; left: 0; width: 849px; top: 338px; text-align: center; color: var(--white); font-weight: 700; font-size: 46px; letter-spacing: 1px; line-height: 62px; }
  .date .weekday { display: inline-flex; width: 46px; height: 46px; border-radius: 50%; background: var(--white); color: var(--label-blue); font-size: 30px; align-items: center; justify-content: center; vertical-align: 6px; margin: 0 8px 0 4px; }
  .venue { position: absolute; left: 0; width: 849px; top: 404px; text-align: center; color: var(--white); font-size: 21px; font-weight: 500; line-height: 32px; }
  .venue .hall { font-size: 25px; font-weight: 700; margin-right: 10px; }

  .person { position: absolute; left: 146px; display: flex; gap: 26px; color: var(--white); }
  .person.chair { top: 454px; }
  .person.speaker { top: 566px; }
  .role-label { flex: none; width: 86px; height: 56px; background: var(--white); color: var(--label-blue); font-size: 27px; font-weight: 700; display: flex; align-items: center; justify-content: center; }
  .person .name { font-size: 44px; font-weight: 700; line-height: 56px; letter-spacing: 3px; }
  .person .name small { font-size: 28px; margin-left: 12px; letter-spacing: 1px; }
  .person .affiliation { font-size: 17px; font-weight: 500; line-height: 1.5; margin-top: 4px; }

  .credits { position: absolute; left: 0; width: 849px; top: 1128px; text-align: center; font-size: 16px; line-height: 1.5; color: var(--ink); }
</style>
</head>
<body>
<main class="flyer">
  <header class="masthead">
    <p class="society-name">SWCA</p>
    <p class="conference-name">第25回嚥下ケア研究会学術大会</p>
    <p class="sponsor-name">ハーモニア</p>
  </header>

  <section class="hero">
    <h1 class="title">これからの<br>摂食嚥下障害看護に<br>何が求められているか</h1>
    <p class="subtitle">〜「機能低下予防」と「終末期care」〜</p>
    <p class="subtitle-en">What is required in the future for dysphagia nursing</p>
    <div class="rule"></div>

    <p class="date">2019年9月7日<span class="weekday">土</span>12:00〜13:00</p>
    <p class="venue"><span class="hall">第8会場</span>(みなと国際会議場 2F 中会議室201)</p>

    <div class="person chair">
      <span class="role-label">座長</span>
      <div>
        <p class="name">森川 佳子<small>先生</small></p>
        <p class="affiliation">北浜看護大学名誉教授</p>
      </div>
    </div>

    <div class="person speaker">
      <span class="role-label">演者</span>
      <div>
        <p class="name">小野 真理<small>先生</small></p>
        <p class="affiliation">公益社団法人みなと看護協会　認定看護師教育課程課程長<br>摂食・嚥下障害看護認定看護師教育課程 主任教員</p>
      </div>
    </div>
  </section>

  <footer class="credits">
    <p>共催</p>
    <p>第25回嚥下ケア研究会学術大会</p>
    <p>ハーモニア株式会社</p>
  </footer>
</main>
</body>
</html>
```